Polish brewery needs BEER LABEL design for WEDDINGS

We need beer label design for weddings. Our brewery is located on South of Poland and it is called Wytwórnia Orlik [PL]/Factory Falcon [ENG]. We feel strong connection to mountains and we use water from the mountain in our vicinity.
Regarding beer style it is India Pale Ale so beer is bitter and aromatic because of high addition of hops. Label design has to be modern and simple. We would prefer bright and cream colors.
We need to have opportunity to edit data which are on the label so we will need to get appropriate files.
In attached files you can find all details. If any additional information will be required please do not hesitate and contact with me.

Target Market(s)

Weddings

Font styles to use
Sans Serif
Script

Colors
ffffff

Requirements
Must have
• Information listed in documents in attached files
Nice to have
• Some nice graphics
Bright and cream colors.
Should not have
• -

```html
<!DOCTYPE html>
<html lang="pl">
<head>
<meta charset="utf-8">
<title>Etykieta weselna – India Pale Ale</title>
<link href="https://fonts.googleapis.com/css2?family=Montserrat:wght@400;500;600;700&family=Pinyon+Script&display=swap" rel="stylesheet">
<style>
  :root {
    --page: #ffffff;
    --cream: #f3e6d9;
    --ink: #2a2523;
    --brown: #7a4a45;
    --rust: #c8825f;
    --hop-tone: #d9bfb2;
    --sprig-tone: #b9aaa2;
  }
  * { margin: 0; padding: 0; box-sizing: border-box; }
  html, body { width: 927px; height: 1200px; overflow: hidden; background: var(--page); }
  body { font-family: "Montserrat", sans-serif; color: var(--ink); position: relative; }

  .label {
    position: absolute; left: 13px; top: 398px; width: 900px; height: 404px;
    background: var(--cream); display: flex;
  }
  .panel { position: relative; width: 300px; height: 100%; }
  .panel + .panel { border-left: 1px solid var(--ink); }

  /* left panel */
  .ingredients {
    position: absolute; left: 13px; top: 19px; width: 275px; height: 84px;
    background: var(--ink); border-radius: 5px; color: var(--cream); text-align: center;
  }
  .ingredients h2 { font-size: 15px; font-weight: 700; letter-spacing: .5px; margin-top: 8px; }
  .ingredients .rule { width: 60px; height: 1px; background: var(--rust); margin: 5px auto 7px; }
  .ingredients p { font-size: 12px; line-height: 15px; }
  .facts { position: absolute; left: 23px; top: 122px; width: 272px; }
  .fact { margin-bottom: 9px; }
  .fact h3 { font-size: 15.5px; font-weight: 600; letter-spacing: .2px; line-height: 19px; }
  .fact p { font-size: 14px; line-height: 17px; padding-left: 3px; letter-spacing: .3px; }
  .brewery {
    position: absolute; left: 27px; top: 307px; width: 235px; height: 81px;
    border: 1px solid var(--ink); padding: 9px 14px;
  }
  .brewery .name { font-size: 13px; font-weight: 600; color: var(--ink); display: flex; align-items: center; gap: 6px; margin-bottom: 6px; }
  .brewery .mark { width: 9px; height: 9px; background: var(--ink); }
  .brewery address { font-style: normal; font-size: 7.5px; font-weight: 600; line-height: 11.5px; }

  /* centre panel */
  .hops-top { position: absolute; right: 0; top: 0; width: 115px; height: 55px;
    background: radial-gradient(ellipse at 70% 30%, var(--hop-tone), transparent 70%); }
  .hops-side { position: absolute; left: 0; top: 27px; width: 33px; height: 110px;
    background: radial-gradient(ellipse at 20% 50%, var(--hop-tone), transparent 72%); }
  .sprig { position: absolute; width: 10px; border-radius: 5px;
    background: linear-gradient(var(--sprig-tone), transparent); opacity: .5; }
  .dot { position: absolute; border-radius: 50%; background: var(--brown); }
  .title { font-family: "Pinyon Script", cursive; font-weight: 400; color: var(--ink); }
  .title span { position: absolute; line-height: 1; white-space: nowrap; }
  .title .l1 { left: 48px; top: 24px; font-size: 80px; }
  .title .l2 { left: 148px; top: 104px; font-size: 46px; }
  .title .l3 { left: 96px; top: 132px; font-size: 80px; }
  .date { position: absolute; top: 234px; width: 100%; text-align: center; font-size: 12px; letter-spacing: 3px; }
  .accent { position: absolute; left: 120px; width: 60px; height: 1px; background: var(--rust); }
  .blurb { position: absolute; top: 286px; left: 30px; width: 240px; text-align: center;
    font-size: 8.3px; font-style: italic; line-height: 11px; color: var(--brown); }
  .style-name { position: absolute; top: 346px; width: 100%; text-align: center;
    font-family: "Pinyon Script", cursive; font-size: 32px; line-height: 1.2; }

  /* right panel */
  .ornament { position: absolute; left: 71px; top: 14px; width: 152px; height: 32px;
    background: linear-gradient(90deg, transparent, var(--hop-tone) 30%, var(--hop-tone) 70%, transparent); border-radius: 16px; }
  .story { position: absolute; left: 26px; top: 62px; width: 246px; font-size: 10.8px;
    line-height: 18px; text-align: justify; text-align-last: justify; color: var(--brown); }
  .badge { position: absolute; width: 70px; text-align: center; }
  .badge svg { display: block; margin: 0 auto; }
  .badge span { display: block; font-size: 9.5px; font-weight: 600; color: var(--brown); margin-top: 6px; }
  .divider { position: absolute; left: 116px; top: 367px; width: 62px; height: 1px; background: var(--rust); }
  .social { position: absolute; left: 14px; top: 378px; width: 280px; display: flex; justify-content: space-between;
    font-size: 7.5px; font-weight: 600; }
  .social span { display: flex; align-items: center; gap: 3px; }
  .social i { width: 9px; height: 9px; border-radius: 50%; background: var(--ink); display: inline-block; }
</style>
</head>
<body>
<main class="label">

  <section class="panel panel-info">
    <div class="ingredients">
      <h2>SKŁADNIKI</h2>
      <div class="rule"></div>
      <p>woda, słód jęczmienny, chmiel,<br>liście limonki, drożdże</p>
    </div>
    <div class="facts">
      <div class="fact"><h3>DATA PRZYDATNOŚCI:</h3><p>00/00/00</p></div>
      <div class="fact"><h3>OBJĘTOŚĆ BUTELKI:</h3><p>330ml</p></div>
      <div class="fact"><h3>WARUNKI PRZECHOWYWANIA:</h3><p>Przechowywać w suchym i<br>ciemnym miejscu.</p></div>
    </div>
    <div class="brewery">
      <div class="name">Wytwórnia Orlik <span class="mark"></span></div>
      <address>34-700 Górna Dolina<br>Browar Klasztorny Sokół<br>Podlesie 12, 34-710 Podlesie</address>
    </div>
  </section>

  <section class="panel panel-front">
    <div class="hops-top" role="img" aria-label="Rysunek szyszek chmielu"></div>
    <div class="hops-side" role="img" aria-label="Rysunek szyszek chmielu"></div>
    <div class="sprig" role="img" aria-label="Gałązka" style="left:272px;top:88px;height:66px;"></div>
    <div class="sprig" role="img" aria-label="Gałązka" style="left:18px;top:238px;height:60px;"></div>
    <div class="sprig" role="img" aria-label="Gałązka" style="left:262px;top:352px;height:36px;"></div>
    <span class="dot" style="left:15px;top:16px;width:3px;height:3px;"></span>
    <span class="dot" style="left:48px;top:52px;width:3px;height:3px;"></span>
    <span class="dot" style="left:30px;top:148px;width:5px;height:5px;"></span>
    <span class="dot" style="left:92px;top:4px;width:3px;height:3px;"></span>
    <span class="dot" style="left:192px;top:30px;width:3px;height:3px;"></span>
    <h1 class="title"><span class="l1">Marek</span><span class="l2">i</span><span class="l3">Ola</span></h1>
    <div class="date">03.12.16</div>
    <div class="accent" style="top:265px;"></div>
    <p class="blurb">Lorem ipsum dolor sit amet, consectetur adipiscing elit, sed do eiusmod tempor incididunt ut labore et dolore magna aliqua.</p>
    <div class="accent" style="top:337px;"></div>
    <div class="style-name">India Pale Ale</div>
  </section>

  <section class="panel panel-story">
    <div class="ornament" role="img" aria-label="Ozdobny ornament roślinny"></div>
    <div class="story"><p>Trzymasz w ręku naszą autorską IPA do produkcji której wykorzystujemy wodę wypływającą z samego serca Beskidu Wysokiego – Babiej Góry. IPA lubi chmiele i goryczkę, ale żeby nie było nudno postanowiliśmy ją wzbogacić limonką.</p></div>

    <div class="badge" style="left:33px;top:190px;">
      <svg width="58" height="58" viewBox="0 0 58 58" fill="none" stroke="var(--brown)" stroke-width="1.6"><circle cx="29" cy="29" r="27.5"/><path d="M27 13h4v7c3 2 4 4 4 7v17h-12V27c0-3 1-5 4-7z"/></svg>
      <span>5,5%</span>
    </div>
    <div class="badge" style="left:111px;top:190px;">
      <svg width="58" height="58" viewBox="0 0 58 58" fill="none" stroke="var(--brown)" stroke-width="1.6"><circle cx="29" cy="29" r="27.5"/><path d="M29 14c-7 5-9 12-9 16 0 6 4 10 9 12 5-2 9-6 9-12 0-4-2-11-9-16zM29 42v4M20 30h18M22 23h14"/></svg>
      <span>MEDIUM</span>
    </div>
    <div class="badge" style="left:189px;top:190px;">
      <svg width="58" height="58" viewBox="0 0 58 58" fill="none" stroke="var(--brown)" stroke-width="1.6"><circle cx="29" cy="29" r="27.5"/><path d="M21 16v28M29 13v31M37 16v28M21 22l-3-3M21 22l3-3M29 20l-3-3M29 20l3-3M37 22l-3-3M37 22l3-3"/></svg>
      <span>PALE</span>
    </div>
    <div class="badge" style="left:69px;top:274px;">
      <svg width="58" height="58" viewBox="0 0 58 58" fill="none" stroke="var(--brown)" stroke-width="1.6"><circle cx="29" cy="29" r="27.5"/><circle cx="17" cy="29" r="5"/><circle cx="37" cy="20" r="7"/><circle cx="32" cy="41" r="3"/></svg>
      <span>14%</span>
    </div>
    <div class="badge" style="left:149px;top:274px;">
      <svg width="58" height="58" viewBox="0 0 58 58" fill="none" stroke="var(--brown)" stroke-width="1.6"><circle cx="29" cy="29" r="27.5"/><path d="M29 12c-6 9-11 15-11 21a11 11 0 0 0 22 0c0-6-5-12-11-21z"/><path d="M21 37l5-6 3 3 3-4 6 7"/></svg>
      <span>WATER</span>
    </div>

    <div class="divider"></div>
    <div class="social">
      <span><i></i>wytworniaorlik</span>
      <span><i></i>wytwornia.orlik</span>
      <span><i></i>www.wytworniaorlik.pl</span>
    </div>
  </section>

</main>
</body>
</html>
```